Quelvo service sheets and folder

A set of 12 Service sheets plus a rate card to be inserted into a folder - each to be designed and formatted.
A4
Portrait
- the idea is to keep things simple and crisp.
I would use the logo (see attached .ai file) at the top and maybe an separate image to go with each sheet

Around 350 words per page (see attached example)
The format is mainly text and bullet points, but each page will be same layout (just a different image as indicated above).

Need to factor in a folder to hold the service sheets.

The documents to have a good sales impact and your experience and advice on best ideas would be welcome. The key is to keep it crisp, elegant & professional for financial services.

The output files should be in PDF and raw file formats so that printing can be managed easily in future., Details for my new Catalogue Design Project will be added soon.

Industry/Entity Type

Financial

Requirements
Must have
• Inspire us!
Should not have
• No images of people or parts (like hands, arms) etc

```html
<!DOCTYPE html>
<html lang="en">
<head>
<meta charset="utf-8">
<title>Quelvo Folder</title>
<link href="https://fonts.googleapis.com/css2?family=Jost:wght@400&family=Open+Sans:wght@400&display=swap" rel="stylesheet">
<style>
  :root {
    --backdrop: #e6e1dc;
    --paper: #ffffff;
    --paper-shade: #ebebeb;
    --ink: #111111;
    --band: #000000;
    --accent-red: #e52d27;
    --accent-green: #6aa338;
    --web-grey: #4a4a4a;
    --faint-mark: #efe7e3;
    --pocket-light: #f7f7f7;
    --pocket-shade: #d9d9d9;
  }
  html, body { margin: 0; padding: 0; overflow: hidden; }
  body { width: 1200px; height: 989px; background: var(--backdrop); }
  .folder { display: block; width: 1200px; height: 989px; }
  .brand-name { font-family: 'Jost', sans-serif; }
  .contact-text { font-family: 'Open Sans', sans-serif; font-size: 13px; fill: var(--paper); }
  .web-address { font-family: 'Open Sans', sans-serif; font-size: 16px; letter-spacing: 3.5px; fill: var(--web-grey); }
</style>
</head>
<body>
<svg class="folder" viewBox="0 0 1200 989" xmlns="http://www.w3.org/2000/svg">
  <defs>
    <linearGradient id="paperFade" x1="0" y1="0" x2="1" y2="1">
      <stop offset="0" stop-color="var(--paper)"/>
      <stop offset="1" stop-color="var(--paper-shade)"/>
    </linearGradient>
    <radialGradient id="pocketFade" cx="0.5" cy="0.45" r="0.75">
      <stop offset="0" stop-color="var(--pocket-light)"/>
      <stop offset="1" stop-color="var(--pocket-shade)"/>
    </radialGradient>
  </defs>

  <!-- open folder inside spread -->
  <g class="spread">
    <rect class="panel-left" x="69" y="30" width="525" height="700" fill="url(#paperFade)"/>
    <rect class="panel-right" x="594" y="30" width="526" height="700" fill="url(#paperFade)"/>
    <line class="spine" x1="594" y1="30" x2="594" y2="660" stroke="#c9c9c9" stroke-width="1.5"/>

    <text class="brand-name faint-name" x="350" y="400" text-anchor="middle" font-size="96" fill="var(--faint-mark)">Quelvo</text>

    <circle class="brand-dot" cx="806" cy="240" r="20" fill="var(--accent-red)"/>
    <text class="brand-name cover-name" x="842" y="262" font-size="54" fill="var(--ink)">QUELVO</text>

    <path class="wave-red" d="M69,596 C250,588 450,610 585,645 C450,622 250,608 69,612 Z" fill="var(--accent-red)"/>
    <path class="wave-green" d="M598,650 C760,682 920,700 1120,676 L1120,690 C920,714 760,692 598,650 Z" fill="var(--accent-green)"/>
    <path class="wave-band" d="M69,620 C300,606 480,640 594,662 C710,686 840,712 1120,700 L1120,730 L69,730 Z" fill="var(--band)"/>
    <path class="wave-line" d="M145,613 C350,608 480,640 594,666 C720,694 860,722 1075,714" fill="none" stroke="var(--paper)" stroke-width="2"/>

    <g class="contact">
      <g class="icon-phone" transform="translate(88,646)">
        <circle cx="6" cy="6" r="6" fill="none" stroke="var(--accent-red)" stroke-width="1.5"/>
        <path d="M3.5,4 q1,4 5,5" fill="none" stroke="var(--accent-red)" stroke-width="1.8"/>
      </g>
      <text class="contact-text" x="105" y="657">+44 (0) 20 7000 4182</text>
      <g class="icon-mail" transform="translate(88,668)">
        <rect x="0" y="1" width="13" height="9" fill="var(--accent-red)"/>
        <path d="M0,1 L6.5,6 L13,1" fill="none" stroke="var(--paper)" stroke-width="1.2"/>
      </g>
      <text class="contact-text" x="105" y="678">info@quelvo.com</text>
      <text class="contact-text" x="88" y="713">12 Harlow Court, London, EC2A 7QT</text>
    </g>

    <text class="web-address" x="780" y="672">www.quelvo.com</text>
  </g>

  <!-- pockets -->
  <path class="pocket-left" d="M24,744 L69,730 L592,730 L576,946 Q574,964 556,964 L69,964 L24,952 Z" fill="url(#pocketFade)"/>
  <text class="brand-name pocket-name" x="300" y="862" text-anchor="middle" font-size="40" fill="var(--ink)">QUELVO</text>

  <path class="pocket-right" d="M596,730 L1120,730 L1166,744 L1166,952 L1120,964 L636,964 Q618,964 616,946 Z" fill="var(--accent-green)"/>
  <text class="brand-name pocket-name" x="870" y="862" text-anchor="middle" font-size="40" fill="var(--paper)">QUELVO</text>
</svg>
</body>
</html>
```